Flyer Design Project

We need a flyer design for a 1 year old domestic cleaning company based in Wiltshire, England. We provide households with high quality, hard working cleaners. We would like to see designs which use blue (the colour on the logo attatched). The final design should communicate a clean, premier and thorough service in a clear and bold way. We would like the flyer to be A5 with a single sided design. We have attached an A5 word document with the words we would like to be used in the design, what we need is for you to give it some life, colour, artwork and a professional touch. We are perfectionsists which we would like to illustrate to our customer through this flyer.
Updates

payment has been guaranteed!

Sorry..... please no pictures of females on the designs. many thanks

Target Market(s)

females with higher than average income, aged 30-50. Have families and work 9-5.

Industry/Entity Type

It Company

Requirements
Must have
• The flyer must include the logo attatched and the words in the A5 document attatched. With RELIABLE CLEANERS preferably the headline. A5 - single sided.
The Flyer must also include our introductory offer.....
First Clean FREE
Allow us to demonstrate our standards

this should be emphasised.

PLEASE NOTE: can this be added to the list of words on the flyer please:

Ironing service - one day turn around
Nice to have
• some pictures - nothing cheesey. Again, pictures should communicate our modern professional approach.

```html
<!DOCTYPE html>
<html lang="en">
<head>
<meta charset="utf-8">
<title>Brookmere Cleaners – Reliable Cleaners Flyer</title>
<link rel="stylesheet" href="https://fonts.googleapis.com/css2?family=Rammetto+One&family=Marcellus&family=Anton&family=Archivo+Black&family=Arimo:wght@700&family=Carlito:wght@400;700&display=swap">
<style>
  :root {
    --blue-deep: #173f8c;
    --blue-mid: #2f6fc4;
    --blue-bright: #3d86d6;
    --blue-pale: #9fd6f2;
    --orange: #f7941d;
    --orange-dark: #e7780c;
    --yellow: #ffe100;
    --white: #ffffff;
    --navy: #14265a;
    --ink: #111111;
    --photo-light: #eee8dc;
    --photo-mid: #c9b79c;
    --photo-dark: #8a6b4c;
    --hero-light: #e3eff4;
    --hero-mid: #a9cbd6;
  }
  * { margin: 0; padding: 0; box-sizing: border-box; }
  html, body { width: 846px; height: 1200px; overflow: hidden; background: #ffffff; }
  .flyer {
    position: relative;
    width: 846px;
    height: 1200px;
    overflow: hidden;
    background: linear-gradient(180deg, var(--blue-deep) 16%, var(--blue-mid) 45%, var(--blue-bright) 70%, var(--blue-deep) 100%);
    font-family: "Arimo", Arial, sans-serif;
  }
  .hero-photo {
    position: absolute; left: 0; top: 0; width: 846px; height: 200px;
    background: linear-gradient(180deg, var(--hero-light) 0%, var(--hero-mid) 60%, #7fb0c6 100%);
  }
  .headline {
    position: absolute; left: 0; top: 58px; width: 846px;
    text-align: center;
    font-family: "Rammetto One", Georgia, serif;
    font-size: 74px; line-height: 1; letter-spacing: 1px;
    color: var(--orange);
    -webkit-text-stroke: 8px var(--white);
    paint-order: stroke fill;
  }
  .offer {
    position: absolute; left: 0; top: 228px; width: 846px;
    text-align: center; white-space: nowrap;
  }
  .offer-lead {
    font-family: "Marcellus", "Optima", serif;
    font-size: 74px; color: var(--white); vertical-align: middle;
  }
  .offer-free {
    display: inline-block; vertical-align: middle;
    margin-left: 8px; padding: 0 10px;
    font-family: "Anton", Impact, sans-serif;
    font-size: 78px; line-height: 1.02; letter-spacing: 2px;
    color: var(--white); background: var(--orange);
  }
  .offer-sub {
    position: absolute; left: 0; top: 318px; width: 846px;
    text-align: center;
    font-family: "Archivo Black", "Arial Black", sans-serif;
    font-size: 29px; color: var(--yellow);
  }
  .showroom {
    position: absolute; left: 0; top: 330px; width: 846px; height: 580px;
  }
  .brand {
    position: absolute; left: 420px; top: 460px; width: 410px;
    font-family: "Carlito", Calibri, sans-serif; color: var(--navy);
  }
  .brand-name { font-size: 50px; font-weight: 700; line-height: 1; }
  .brand-tag { font-size: 24px; font-weight: 700; color: var(--ink); margin-top: 14px; margin-left: 84px; }
  .features {
    position: absolute; top: 896px; list-style: none;
    font-size: 23px; line-height: 29px; color: var(--white);
  }
  .features li::before {
    content: ""; display: inline-block; width: 9px; height: 9px; border-radius: 50%;
    background: var(--yellow); margin-right: 6px; vertical-align: middle;
    position: relative; top: -2px;
  }
  .features-left { left: 32px; }
  .features-right { left: 523px; }
  .contact-email {
    position: absolute; left: 0; top: 996px; width: 846px;
    text-align: center; color: var(--yellow); font-size: 25px; line-height: 34px;
  }
  .contact-phone {
    position: absolute; left: 0; top: 1080px; width: 846px;
    text-align: center;
    font-family: "Rammetto One", Georgia, serif;
    font-size: 58px; letter-spacing: 2px;
    color: var(--orange);
    -webkit-text-stroke: 7px var(--white);
    paint-order: stroke fill;
  }
  .contact-phone .label { margin-right: 28px; }
</style>
</head>
<body>
<main class="flyer">
  <div class="hero-photo" role="img" aria-label="Photo of a gloved hand holding a spray bottle while cleaning"></div>
  <h1 class="headline">Reliable&nbsp; Cleaners!</h1>

  <p class="offer"><span class="offer-lead">First Clean</span><span class="offer-free">FREE</span></p>
  <p class="offer-sub">Allow Us To Demonstrate Our Standards......</p>

  <svg class="showroom" width="846" height="580" viewBox="0 330 846 580" role="img" aria-label="Photo of a bright, tidy living room with sofa, fireplace, rug and coffee table">
    <defs>
      <linearGradient id="room-tones" x1="0" y1="0" x2="1" y2="1">
        <stop offset="0" stop-color="var(--photo-light)"/>
        <stop offset="0.55" stop-color="var(--photo-mid)"/>
        <stop offset="1" stop-color="var(--photo-dark)"/>
      </linearGradient>
    </defs>
    <path d="M0,372 C250,402 520,392 846,342 L846,372 C520,420 250,440 0,412 Z" fill="var(--blue-pale)"/>
    <path d="M0,412 C250,440 520,420 846,372 L846,822 C600,800 300,850 0,880 Z" fill="url(#room-tones)"/>
    <path d="M0,880 C300,850 600,800 846,822 L846,842 C600,822 300,872 0,900 Z" fill="var(--blue-pale)"/>
  </svg>

  <div class="brand">
    <div class="brand-name">Brookmere Cleaners</div>
    <div class="brand-tag">Premier Domestic Cleaners</div>
  </div>

  <ul class="features features-left">
    <li>Ironing Service - One Day Turn Around</li>
    <li>Constantly Thorough</li>
    <li>Insured</li>
    <li>No Contracts</li>
  </ul>
  <ul class="features features-right">
    <li>Personalised Service</li>
    <li>Hassel Free</li>
    <li>Regular Weekly Cleans</li>
  </ul>

  <p class="contact-email">Email:<br>brookmerecleaners@mailbox.co.uk</p>
  <p class="contact-phone"><span class="label">Tele:</span>07700900461</p>
</main>
</body>
</html>
```